Letterhead design for Sleep Consulting Business

I'm looking for a new letterhead (heading/footer) design for my Sleep Consulting Business, I work with families to help their children improve their sleep.

The heading/footer will used in Microsoft Word Only-to be used for all of my documents such as writing Sleep Plans. I need to utilize as much working space in the document as possible. This will NOT be printed out on paper- it will only be used for heading/footer on microsoft word, then emailed to clients, who may print it at home.

My brand colors:
Dark Blue Hex: 1F2A42
Lighter Blueish Hex: 90BEC9
You're welcome to check out my website for inspiration- it is freshly created with other colors as well, and I love the outcome. www.quietharborsleep.example

Target Market(s)

Tired parents

Font styles to use
Script
Other font styles liked:
• Great Vibe, Lato or Just Another Hand are all used currently for my brand. Open to other options.

Requirements
Must have
• The letterhead (heading/footer) MUST be kept narrow (height-wise), so I have plenty of space on my document, while including important information.

It should look professional on screen, and when printed.

Must include my business name OR logo (Quiet Harbor Sleep Consulting), and my email address. Tessa@quietharborsleep.example

Website is optional, not required, just if you need to fill in a spot: www.quietharborsleep.example

```html
<!DOCTYPE html>
<html lang="en">
<head>
<meta charset="utf-8">
<title>Quiet Harbor Sleep Consulting – Letterhead</title>
<link rel="stylesheet" href="https://fonts.googleapis.com/css2?family=Great+Vibes&family=Lato:wght@400;700&display=swap">
<style>
  :root {
    --navy: #1f2a42;
    --sky: #6fb3d6;
    --paper: #f6fbfe;
    --backdrop: #9fd4de;
  }
  * { margin: 0; padding: 0; box-sizing: border-box; }
  html, body {
    width: 1200px;
    height: 1000px;
    overflow: hidden;
    background: var(--backdrop);
  }
  .letterhead {
    position: absolute;
    left: 270px;
    top: 34px;
    width: 660px;
    height: 932px;
    background: var(--paper);
    box-shadow: 0 6px 18px rgba(31, 42, 66, 0.18);
    overflow: hidden;
  }
  .letterhead__waves {
    position: absolute;
    inset: 0;
    width: 660px;
    height: 932px;
  }
  .brand {
    position: absolute;
    left: 28px;
    top: 44px;
    display: flex;
    align-items: center;
    gap: 8px;
  }
  .brand__dot {
    width: 28px;
    height: 28px;
    border-radius: 50%;
    background: var(--navy);
  }
  .brand__name {
    font-family: "Great Vibes", cursive;
    font-size: 22px;
    font-weight: 400;
    color: var(--navy);
    line-height: 1;
  }
  .contact {
    position: absolute;
    left: 336px;
    bottom: 60px;
    list-style: none;
    font-family: "Lato", sans-serif;
    font-weight: 700;
    font-size: 10px;
    color: var(--navy);
    line-height: 1.6;
  }
  .contact__item {
    display: flex;
    align-items: center;
    gap: 6px;
  }
  .contact__icon {
    width: 10px;
    height: 10px;
    flex: none;
  }
</style>
</head>
<body>
  <main class="letterhead">
    <svg class="letterhead__waves" viewBox="0 0 660 932" aria-hidden="true">
      <!-- header accent -->
      <path d="M250,0 C390,22 560,26 660,82 V0 Z" fill="var(--sky)"/>
      <path d="M250,0 C390,22 560,26 660,82 V90 C560,34 390,28 250,0 Z" fill="var(--navy)"/>
      <path d="M555,0 H660 V46 C628,20 596,8 555,0 Z" fill="var(--navy)"/>
      <!-- footer accent -->
      <path d="M0,872 C150,882 300,916 450,906 C560,899 620,872 660,856 V932 H0 Z" fill="var(--sky)"/>
      <path d="M0,866 C150,876 300,910 450,900 C560,893 620,866 660,850 V856 C620,872 560,899 450,906 C300,916 150,882 0,872 Z" fill="var(--navy)"/>
      <path d="M0,932 V872 C55,886 105,908 140,932 Z" fill="var(--navy)"/>
    </svg>

    <header class="brand">
      <span class="brand__dot"></span>
      <span class="brand__name">Quiet Harbor Sleep Consulting</span>
    </header>

    <ul class="contact">
      <li class="contact__item">
        <svg class="contact__icon" viewBox="0 0 12 12" aria-hidden="true">
          <rect x="0.75" y="2.25" width="10.5" height="7.5" fill="none" stroke="var(--navy)" stroke-width="1.2"/>
          <path d="M1,2.75 L6,6.8 L11,2.75" fill="none" stroke="var(--navy)" stroke-width="1.2"/>
        </svg>
        <span>Tessa@quietharborsleep.example</span>
      </li>
      <li class="contact__item">
        <svg class="contact__icon" viewBox="0 0 12 12" aria-hidden="true">
          <circle cx="6" cy="6" r="5.2" fill="none" stroke="var(--navy)" stroke-width="1.2"/>
          <ellipse cx="6" cy="6" rx="2.3" ry="5.2" fill="none" stroke="var(--navy)" stroke-width="1"/>
          <path d="M0.8,6 H11.2" stroke="var(--navy)" stroke-width="1"/>
        </svg>
        <span>www.quietharborsleep.example</span>
      </li>
    </ul>
  </main>
</body>
</html>
```